Mirrorglow 90's Revival club night

I am after either an A5 or DL flyer but also the formats for using the design on social media etc.
The flyer is for a 90's revival club night at a nightclub that was well attended in the 90's . A special guest PA - Honey Q famous for her single 'Carry me through the starlight' ,is performing.
I have a logo for the night that may have to be altered / edited to fit in with your design (Colours changed etc) but also have a logo for the artist that may be more restrictive in regards to any changes.Both are attached.
Look forward to hearing from you shortly,

Tam

Reason: Required text to go on the flyer has now be added to the brief. Majority of designs submitted didn't seem to reflect to '90's nightclub' feel we were hoping for. Most of the designs used the colour scheme based on the 'Mirrorglow' logo. We are hoping that these colours can be ignored with some designs and that the logo is made of of different colours that would make it easier for it to fit in with the designers ideas. Regards Tam

Target Market(s)

20 to 50 years age range who use to go clubbing / still do / love the 90's music. Club that they use to attend in the 90's is where the event is being held

Industry/Entity Type

Club

Requirements
Must have
• Both the logos for the event ( Mirrorglow 90's Revival and Honey Q ) must be included on the flyer. Colours and the format can be altered on the mirrorglow logo but the design should remain as close to the original as sent. 90's font and images would also be a must if possible. Honey Q logo can have colors altered, but not the font or design.
• Text required as follows :
• Venue : Club Orbit, Pellingford Lane, Westbury, Wiltshire
• Date : Saturday 10th June 2017
• Time : 8.30pm till 3am
• Very special guest PA ‘ HONEY Q’ ‘Carry me through the starlight’
• DJ’s : Main room – Danny Holtsby ( Arcade 77 / Mirrorglow )
• Room 2 – Simon P
• Full club décor with Laser lightshow, CO’2 cannons and pryrotechnics
• Tickets : £15 VIP / £10 General Admission – Available from : https://www.passgate-example.co.uk/venue/QZTRWN
• Or ‘Club Orbit’ : 01632 960418
• Web : www.ravebackclub-example.co.uk
Nice to have
• open to ideas
Should not have
• Not to cheesy ........

```html
<!DOCTYPE html>
<html lang="en">
<head>
<meta charset="utf-8">
<title>Mirrorglow 90's Revival – Club Night Flyer</title>
<link href="https://fonts.googleapis.com/css2?family=Oswald:wght@400;600;700&family=Russo+One&family=Yellowtail&display=swap" rel="stylesheet">
<style>
:root{
  --bg:#050507;
  --white:#ffffff;
  --silver:#d9dde3;
  --red:#e3202a;
  --yellow:#ffd21f;
  --cyan:#26d3f0;
  --bar:#1b1c22;
}
*{margin:0;padding:0;box-sizing:border-box}
html,body{width:893px;height:1200px;overflow:hidden;background:var(--bg)}
body{font-family:'Oswald',sans-serif;color:var(--white)}
.flyer{position:relative;width:893px;height:1200px;overflow:hidden;
  background:radial-gradient(ellipse at 50% 40%,#1a1030 0%,var(--bg) 65%)}
.glow-art{position:absolute;left:90px;top:200px;width:713px;height:470px;border-radius:50%;
  background:radial-gradient(ellipse at 50% 50%,rgba(255,138,28,.55) 0%,rgba(212,42,168,.45) 30%,rgba(38,211,240,.3) 55%,rgba(5,5,7,0) 72%)}
.brand{position:absolute;top:40px;display:flex;align-items:center;gap:14px;
  font-weight:700;color:var(--cyan);font-size:34px;letter-spacing:1px}
.brand-night{left:40px;width:340px;line-height:1.05}
.brand-artist{right:50px;color:var(--white);font-size:52px}
.brand-mark{width:22px;height:22px;background:var(--yellow);flex:none}
.headline{position:absolute;left:0;right:0;top:215px;text-align:center}
.headline-the{font-family:'Yellowtail',cursive;font-size:110px;color:var(--silver);
  position:absolute;left:255px;top:0;text-shadow:0 0 14px rgba(0,0,0,.8)}
.headline-90s{font-family:'Russo One',sans-serif;font-size:330px;line-height:1;margin-top:70px;
  background:linear-gradient(180deg,#ffffff 0%,#c9ced6 45%,#6e737c 52%,#e9ecef 100%);
  -webkit-background-clip:text;background-clip:text;color:transparent;letter-spacing:-6px}
.headline-revival{font-weight:700;font-size:34px;letter-spacing:14px;color:var(--white);margin-top:-20px}
.details{position:absolute;left:30px;right:30px;top:700px;display:flex;align-items:stretch;height:112px}
.details > div{padding:0 18px}
.details > div + div{border-left:3px solid var(--white)}
.when{width:235px}
.when-time{font-size:20px;font-weight:600}
.when-date{font-size:54px;font-weight:700;line-height:1}
.when-day{font-size:22px;font-weight:600;letter-spacing:2px}
.djs{width:260px;font-size:15px;line-height:1.25;white-space:nowrap}
.djs-label{font-size:30px;font-weight:700;line-height:1.05}
.djs-label .accent{font-size:16px}
.djs-name{font-size:24px;font-weight:700}
.djs .accent{color:var(--red);font-weight:600}
.venue{flex:1}
.venue-name{font-size:56px;font-weight:700;line-height:1}
.venue-address{font-size:25px;font-weight:600;line-height:1.2}
.guest{position:absolute;left:0;right:0;top:832px;text-align:center;font-size:24px;font-weight:700;white-space:nowrap}
.guest .accent{color:var(--red)}
.decor{position:absolute;left:0;right:0;top:878px;text-align:center;font-size:22px;font-weight:600;color:var(--yellow);white-space:nowrap}
.tickets{position:absolute;left:0;right:0;top:918px;text-align:center;font-size:36px;font-weight:700}
.tickets .accent{color:var(--yellow)}
.tickets small{font-size:28px;font-weight:600}
.availability{position:absolute;left:0;right:0;top:976px;text-align:center;font-size:22px;font-weight:400;color:var(--silver);line-height:1.35}
.footer{position:absolute;left:0;right:0;bottom:0;height:70px;background:var(--bar);
  border-top:4px solid var(--red);display:flex;align-items:center;justify-content:space-between;padding:0 36px;font-size:24px}
.follow{display:flex;align-items:center;gap:10px;font-size:20px}
.follow .dot{width:28px;height:28px;background:var(--red);border-radius:4px}
</style>
</head>
<body>
<main class="flyer">
  <div class="glow-art" role="img" aria-label="Glowing rainbow light burst behind the headline"></div>

  <div class="brand brand-night"><span class="brand-mark"></span><span>Mirrorglow 90's Revival</span></div>
  <div class="brand brand-artist">Honey Q</div>

  <header class="headline">
    <div class="headline-the">The</div>
    <div class="headline-90s">90s</div>
    <div class="headline-revival">REVIVAL</div>
  </header>

  <section class="details">
    <div class="when">
      <div class="when-time">TIME : 8:30 PM - 3 AM</div>
      <div class="when-date">10.06.17</div>
      <div class="when-day">SATURDAY</div>
    </div>
    <div class="djs">
      <div class="djs-label">DJ : <span class="accent">MAIN ROOM</span></div>
      <div class="djs-name">DANNY HOLTSBY</div>
      <div class="accent">( ARCADE 77 | MIRRORGLOW )</div>
      <div><span class="accent">ROOM 2 :</span> <b>SIMON P</b></div>
    </div>
    <div class="venue">
      <div class="venue-name">CLUB ORBIT</div>
      <div class="venue-address">PELLINGFORD LANE</div>
      <div class="venue-address">WESTBURY, WILTSHIRE</div>
    </div>
  </section>

  <p class="guest">VERY SPECIAL GUEST PA <span class="accent">'HONEY Q'</span> 'CARRY ME THROUGH THE STARLIGHT'</p>
  <p class="decor">Full club décor with Laser lightshow, CO'2 cannons and pyrotechnics</p>
  <p class="tickets"><span class="accent">TICKETS :</span> £15 VIP / £10 <small>General Admission</small></p>
  <p class="availability">Available from : https://www.passgate-example.co.uk/venue/QZTRWN<br>Or 'Club Orbit' : 01632 960418</p>

  <footer class="footer">
    <div>Website : www.ravebackclub-example.co.uk</div>
    <div class="follow">Follow us : <span class="dot"></span><span class="dot"></span><span class="dot"></span><span class="dot"></span></div>
  </footer>
</main>
</body>
</html>
```